Nordavexa - world unique technology for better life - please let them know who am i at first sight

We need a new business card for company which is a provider of unique crystal based technology suitable for all living being. For more information and final design you can use our brochure (our colours are black and blue from brochure).
We use Verdana font

Industry/Entity Type

Business

Contact Information for Business Card

regular dimension

Other font styles liked:
• Verdana

Requirements
Must have
• Logo
• name
• function/position
• phone
• mobile
• e-mail
• adress
Nice to have
• inovative design (technology directed)

```html
<!DOCTYPE html>
<html lang="en">
<head>
<meta charset="utf-8">
<title>Nordavexa Business Card</title>
<link rel="stylesheet" href="https://fonts.googleapis.com/css2?family=Noto+Sans:wght@300;700&display=swap">
<style>
  :root {
    --backdrop: #d9dadb;
    --brand-blue: #0fa0dc;
    --brand-blue-light: #2cb3e8;
    --brand-blue-deep: #0a8fcb;
    --paper: #f4f4f2;
    --ink-white: #ffffff;
    --pattern-tint: #9fd6ef;
    --shadow: rgba(0, 0, 0, 0.18);
  }
  * { margin: 0; padding: 0; box-sizing: border-box; }
  html, body {
    width: 1200px;
    height: 1000px;
    overflow: hidden;
    background: var(--backdrop);
  }
  .canvas {
    position: relative;
    width: 1200px;
    height: 1000px;
  }
  .card {
    position: absolute;
    left: 250px;
    width: 700px;
    height: 400px;
    overflow: hidden;
    box-shadow: 0 6px 18px var(--shadow);
  }

  /* Back of card */
  .card-back {
    top: 50px;
    background: linear-gradient(160deg, var(--brand-blue-light), var(--brand-blue-deep));
  }
  .card-back .brand {
    position: absolute;
    left: 110px;
    top: 160px;
    display: flex;
    align-items: center;
    gap: 26px;
  }
  .card-back .brand-dot {
    width: 70px;
    height: 70px;
    border-radius: 50%;
    background: var(--ink-white);
  }
  .card-back .brand-name {
    font-family: Verdana, "Noto Sans", sans-serif;
    font-weight: 300;
    font-size: 52px;
    letter-spacing: 4px;
    color: var(--ink-white);
  }

  /* Front of card */
  .card-front {
    top: 520px;
    background: var(--brand-blue);
  }
  .card-front .shapes {
    position: absolute;
    inset: 0;
  }
  .card-front .brand {
    position: absolute;
    left: 30px;
    top: 150px;
    display: flex;
    align-items: center;
    gap: 14px;
  }
  .card-front .brand-dot {
    width: 46px;
    height: 46px;
    border-radius: 50%;
    background: var(--brand-blue);
  }
  .card-front .brand-name {
    font-family: Verdana, "Noto Sans", sans-serif;
    font-weight: 300;
    font-size: 30px;
    letter-spacing: 2px;
    color: var(--brand-blue);
  }
  .identity {
    position: absolute;
    left: 400px;
    top: 133px;
    width: 220px;
    text-align: center;
    font-family: Verdana, "Noto Sans", sans-serif;
    font-weight: 700;
    color: var(--brand-blue);
  }
  .identity .person-name { font-size: 26px; line-height: 32px; }
  .identity .person-role { font-size: 18px; line-height: 22px; }
  .contact {
    position: absolute;
    right: 30px;
    top: 262px;
    text-align: right;
    font-family: Verdana, "Noto Sans", sans-serif;
    font-weight: 700;
    font-size: 17px;
    line-height: 25px;
    color: var(--ink-white);
    list-style: none;
  }
  .contact .address { margin-top: 6px; }
</style>
</head>
<body>
<main class="canvas">

  <section class="card card-back" aria-label="Business card back">
    <div class="brand">
      <span class="brand-dot"></span>
      <span class="brand-name">NORDAVEXA</span>
    </div>
  </section>

  <section class="card card-front" aria-label="Business card front">
    <svg class="shapes" width="700" height="400" viewBox="0 0 700 400" aria-hidden="true">
      <circle cx="120" cy="170" r="300" fill="var(--paper)"/>
      <path d="M300 128 H600 A42 42 0 0 1 600 212 H300 Z" fill="var(--paper)"/>
    </svg>
    <svg class="shapes" width="700" height="400" viewBox="0 0 700 400">
      <defs>
        <linearGradient id="pattern-fade" x1="0" y1="0" x2="1" y2="0">
          <stop offset="0" stop-color="var(--pattern-tint)" stop-opacity="0.9"/>
          <stop offset="1" stop-color="var(--pattern-tint)" stop-opacity="0.5"/>
        </linearGradient>
      </defs>
      <rect role="img" aria-label="Decorative crystal lattice pattern" x="60" y="0" width="280" height="95" rx="30" fill="url(#pattern-fade)"/>
      <rect role="img" aria-label="Decorative crystal lattice pattern" x="0" y="275" width="300" height="125" rx="30" fill="url(#pattern-fade)"/>
    </svg>

    <div class="brand">
      <span class="brand-dot"></span>
      <span class="brand-name">NORDAVEXA</span>
    </div>

    <div class="identity">
      <div class="person-name">Your Name</div>
      <div class="person-role">Position</div>
    </div>

    <ul class="contact">
      <li>Phone : 012- 345- 6789</li>
      <li>Mobile : 098- 765- 4321</li>
      <li>Email : yourname@mail.com</li>
      <li class="address">Address which you want to provide</li>
    </ul>
  </section>

</main>
</body>
</html>
```